Notary Signing Agent Need Business card Design

Need a Business card design for my new company. RT Belvoni-Strand LLC
Mobile Notary Signing Agent. I go to the customer for closing of Mortgage's Documents . possible signs of honesty, integrity and confidentiality.

Work with Title company to Notary Mortgage closing.

My Target Market is Title companies. Banks and Financial Institution.

Color Blue to Black Professional ) if needed some Green Little Red

And possible a company logo.

Mobile ( travel to clients ) Integrity, Honest Trustworthy. A show of Professional services.

Would like company name and my name on card

Use both sides and front with business name and my name. phone numbers.

Target Market(s)

Title company, Banks mortgage company

Industry/Entity Type

Travel

Contact Information for Business Card

Notary, Certified signing agent, Mobile

Colors
0455a3

Requirements
Must have
• Name of company , owners name phone number,
Nice to have
• blue and black color like a professional look but not limit to these only.
• a stand out from other cards .

```html
<!DOCTYPE html>
<html lang="en">
<head>
<meta charset="utf-8">
<title>RT Belvoni-Strand LLC — Business Card</title>
<link rel="stylesheet" href="https://fonts.googleapis.com/css2?family=Questrial&display=swap">
<style>
  :root {
    --backdrop: #5e5f60;
    --card: #ededeb;
    --ink: #1b1b1b;
    --brand-blue: #0455a3;
    --card-shadow: rgba(0, 0, 0, 0.35);
  }
  * { box-sizing: border-box; margin: 0; padding: 0; }
  html, body {
    width: 1200px;
    height: 799px;
    overflow: hidden;
    background: var(--backdrop);
    font-family: "Questrial", "Century Gothic", sans-serif;
  }
  .stage {
    position: relative;
    width: 1200px;
    height: 799px;
    display: flex;
    align-items: center;
    justify-content: center;
    gap: 48px;
  }
  .card {
    width: 525px;
    height: 300px;
    background: var(--card);
    box-shadow: 0 14px 30px var(--card-shadow);
    display: flex;
    flex-direction: column;
    align-items: center;
  }
  .card--front { justify-content: center; }
  .brand-lockup {
    display: flex;
    align-items: center;
    gap: 12px;
  }
  .brand-mark {
    width: 14px;
    height: 14px;
    background: var(--brand-blue);
  }
  .brand-name {
    font-size: 26px;
    color: var(--ink);
    letter-spacing: 0.5px;
  }
  .card--back { padding-top: 48px; }
  .company-name {
    font-size: 19px;
    color: var(--brand-blue);
    letter-spacing: 0.3px;
  }
  .owner-name {
    margin-top: 50px;
    font-size: 26px;
    color: var(--ink);
    letter-spacing: 0.4px;
  }
  .contact-list {
    list-style: none;
    margin-top: 14px;
    text-align: center;
    font-size: 16px;
    line-height: 1.2;
    color: var(--ink);
  }
</style>
</head>
<body>
  <main class="stage">
    <section class="card card--front" aria-label="Card front">
      <div class="brand-lockup">
        <span class="brand-mark" aria-hidden="true"></span>
        <span class="brand-name">RT Belvoni-Strand LLC</span>
      </div>
    </section>
    <section class="card card--back" aria-label="Card back">
      <p class="company-name">RT Belvoni-Strand LLC.</p>
      <p class="owner-name">Daniel R Hollis</p>
      <ul class="contact-list">
        <li>C: 555-014-2260</li>
        <li>F: 555-018-3391</li>
      </ul>
    </section>
  </main>
</body>
</html>
```